Presentation Folder with inside Pockets

We need a Presentation Folder with inside pockets. The size of the folder will be 9" x 12" and will be printed on the cover, the back and the inside folder flaps. The design will be very simple and consist of our logo (large) on the front cover and our logo (smaller) and contact information on the back. We are open to various colors that you think may go along with our logo. When you display your work, show the front, back and inside.

Target Market(s)

Pharmaceutical Companies

Industry/Entity Type

Work

Requirements
Should not have
• please do not add stock medical photos.

```html
<!DOCTYPE html>
<html lang="en">
<head>
<meta charset="utf-8">
<title>Meridian Trials Inc. — Presentation Folder</title>
<link href="https://fonts.googleapis.com/css2?family=Open+Sans:wght@400;600;700&display=swap" rel="stylesheet">
<style>
  :root {
    --stage: #000000;
    --blue-light: #1b9ad9;
    --blue-mid: #1a6fa8;
    --blue-deep: #0f4574;
    --accent-green: #8cc63f;
    --green-deep: #5f9b2f;
    --pocket-grey: #e9e9e9;
    --paper: #ffffff;
    --ink: #1a1a1a;
    --ink-soft: #555555;
    --faint-circle: #eef3e6;
    --die-line: #9a9a9a;
  }
  * { box-sizing: border-box; margin: 0; padding: 0; }
  html, body { width: 1200px; height: 975px; overflow: hidden; background: var(--stage); }
  body { font-family: "Open Sans", Arial, sans-serif; position: relative; }

  .folder { position: absolute; inset: 0; }

  .pockets { position: absolute; left: 0; top: 0; }

  .back-cover {
    position: absolute; left: 105px; top: 42px; width: 507px; height: 676px;
    background: linear-gradient(to bottom, var(--blue-light) 0%, var(--blue-mid) 45%, var(--blue-deep) 100%);
    color: var(--paper); text-align: center;
  }
  .back-cover .brand-dot {
    position: absolute; left: 203px; top: 441px; width: 100px; height: 100px;
    border-radius: 50%; background: var(--paper);
  }
  .back-cover .brand-name {
    position: absolute; left: 0; right: 0; top: 549px;
    font-weight: 700; font-size: 26px; letter-spacing: 1px; line-height: 1.15;
  }
  .back-cover .contact-line {
    position: absolute; left: 0; right: 0; font-size: 12.5px; color: var(--paper);
    display: flex; justify-content: center; align-items: center; gap: 6px;
  }
  .back-cover .contact-line.first { top: 621px; }
  .back-cover .contact-line.second { top: 643px; }
  .contact-line svg { width: 12px; height: 12px; }

  .front-cover {
    position: absolute; left: 612px; top: 42px; width: 508px; height: 676px;
    background: var(--paper); overflow: hidden;
  }
  .front-cover .tab-green {
    position: absolute; left: 0; top: 0; width: 55px; height: 30px;
    background: linear-gradient(to right, var(--accent-green), var(--green-deep));
  }
  .front-cover .tab-blue {
    position: absolute; left: 66px; top: 0; right: 0; height: 30px;
    background: linear-gradient(to right, var(--blue-light), var(--blue-deep));
  }
  .front-cover .faint-circle {
    position: absolute; left: 70px; top: 175px; width: 380px; height: 380px;
    border-radius: 50%; background: var(--faint-circle);
  }
  .front-cover .brand-name {
    position: absolute; left: 40px; right: 20px; top: 310px;
    font-weight: 700; font-size: 30px; color: var(--ink); letter-spacing: 1px;
    text-align: center; line-height: 1.2;
  }
  .front-cover .web-band {
    position: absolute; left: 0; right: 0; bottom: 0; height: 28px;
    background: linear-gradient(to right, var(--blue-deep), var(--blue-mid) 50%, var(--blue-light));
    color: var(--paper); font-size: 12.5px; letter-spacing: 2px;
    display: flex; align-items: center; justify-content: center;
  }
  .web-band strong { font-weight: 700; }

  .business-card {
    position: absolute; top: 779px; height: 114px;
    background: var(--paper); border: 1px solid #d0d0d0;
    font-size: 5.5px; color: var(--ink-soft);
  }
  .business-card.left { left: 237px; width: 206px; }
  .business-card.right { left: 786px; width: 197px; }
  .business-card .card-brand {
    position: absolute; left: 10px; top: 17px; display: flex; align-items: center; gap: 4px;
    font-weight: 700; font-size: 8px; color: var(--ink);
  }
  .card-brand .dot { width: 16px; height: 16px; border-radius: 50%; background: var(--accent-green); }
  .business-card .card-contact { position: absolute; left: 11px; top: 63px; line-height: 10px; }
  .business-card .card-address { position: absolute; left: 11px; top: 90px; line-height: 8px; }
  .business-card .card-person { position: absolute; right: 28px; top: 66px; text-align: center; line-height: 8px; }
  .card-slits { position: absolute; left: 0; top: 0; }
</style>
</head>
<body>
<main class="folder">
  <svg class="pockets" width="1200" height="975" viewBox="0 0 1200 975" aria-hidden="true">
    <defs>
      <radialGradient id="greyPocket" cx="0.55" cy="0.4" r="0.8">
        <stop offset="0" stop-color="#ffffff"/>
        <stop offset="1" stop-color="#d9d9d9"/>
      </radialGradient>
      <radialGradient id="greenPocket" cx="0.5" cy="0.55" r="0.75">
        <stop offset="0" stop-color="#a8d05a"/>
        <stop offset="1" stop-color="#6aa336"/>
      </radialGradient>
    </defs>
    <path d="M62 731 L105 718 L612 718 L612 925 Q610 944 590 944 L80 944 Q62 944 62 926 Z" fill="url(#greyPocket)"/>
    <path d="M612 718 L1120 718 L1163 731 L1163 926 Q1163 944 1145 944 L632 944 Q612 944 612 925 Z" fill="url(#greenPocket)"/>
  </svg>

  <section class="back-cover" aria-label="Back cover">
    <div class="brand-dot"></div>
    <p class="brand-name">MERIDIAN TRIALS INC.</p>
    <p class="contact-line first">
      <svg viewBox="0 0 12 12"><circle cx="6" cy="6" r="5.3" fill="none" stroke="#fff"/><path d="M4 3.5 L5 5.5 L4.6 6 Q5.4 7.6 6.8 8 L7.4 7.4 L9 8.4" fill="none" stroke="#fff" stroke-width="1"/></svg>
      +1-555-013-2748
      <svg viewBox="0 0 12 12" style="margin-left:8px"><rect x="1" y="3" width="10" height="7" fill="#fff"/><path d="M1 3 L6 7 L11 3" fill="none" stroke="#1a5f92"/></svg>
      hello@meridiantrials.net
    </p>
    <p class="contact-line second">Meridian Trials, Inc. 214 Linden Avenue, Fairview, NY 10599</p>
  </section>

  <section class="front-cover" aria-label="Front cover">
    <div class="tab-green"></div>
    <div class="tab-blue"></div>
    <div class="faint-circle"></div>
    <p class="brand-name">MERIDIAN TRIALS INC.</p>
    <p class="web-band">www.<strong>meridiantrials</strong>.net</p>
  </section>

  <article class="business-card left" aria-label="Business card">
    <div class="card-brand"><span class="dot"></span>MERIDIAN TRIALS INC.</div>
    <p class="card-contact">☎ +1-555-013-2748<br>✉ hello@meridiantrials.net</p>
    <p class="card-address">Meridian Trials, Inc. 214 Linden Avenue<br>Fairview, NY 10599</p>
    <p class="card-person">Your Name<br>Title</p>
  </article>

  <article class="business-card right" aria-label="Business card">
    <div class="card-brand"><span class="dot"></span>MERIDIAN TRIALS INC.</div>
    <p class="card-contact">☎ +1-555-013-2748<br>✉ hello@meridiantrials.net</p>
    <p class="card-address">Meridian Trials, Inc. 214 Linden Avenue<br>Fairview, NY 10599</p>
    <p class="card-person">Your Name<br>Title</p>
  </article>

  <svg class="card-slits" width="1200" height="975" viewBox="0 0 1200 975" aria-hidden="true">
    <g stroke="var(--die-line)" stroke-width="1">
      <line x1="230" y1="793" x2="252" y2="771"/><line x1="428" y1="771" x2="450" y2="793"/>
      <line x1="230" y1="879" x2="252" y2="901"/><line x1="428" y1="901" x2="450" y2="879"/>
      <line x1="779" y1="793" x2="801" y2="771"/><line x1="968" y1="771" x2="990" y2="793"/>
      <line x1="779" y1="879" x2="801" y2="901"/><line x1="968" y1="901" x2="990" y2="879"/>
    </g>
  </svg>
</main>
</body>
</html>
```